One Page flat design for Car Classified Site

I'm looking for a flat design that that is very simple on the eye but with style. I need it to have a footer for some links etc, and the header needs a new feel but nothing to major.
This one page design is needed for the main page of the classified site...after this page is correct then all the other pages need to be designed to follow a similar style (new work).
I want more emphasis on the text rather than the images as a lot of users don't add images of the vehicles.
Attached is a mock up of the information and rough layout.
Motorbayhub.com is a classified site for car dealers only, I've also attached how the main competitions site looks.
Target Market(s)
Middle aged men, these guys are car dealers so it needs to be basic and easy for them as they aren't techie types.
Industry/Entity Type
Work
Number of Pages Required
1 page
Font styles to use
Look and feel

```html
<!DOCTYPE html>
<html lang="en">
<head>
<meta charset="utf-8">
<title>Motorbayhub – Search Results</title>
<link rel="stylesheet" href="https://fonts.googleapis.com/css2?family=Open+Sans:ital,wght@0,300;0,400;0,600;0,700;1,300&display=swap">
<style>
  :root {
    --green: #4fae0e;
    --green-text: #5cb320;
    --ink: #1c1c1c;
    --muted: #b9b9b9;
    --page: #ecede6;
    --card: #f4f4f4;
    --card-line: #dedede;
    --white: #ffffff;
    --button: #1e1e1e;
    --social: #6d6d6d;
  }
  * { box-sizing: border-box; margin: 0; padding: 0; }
  html, body {
    width: 1030px; height: 1200px; overflow: hidden;
    font-family: "Open Sans", Arial, sans-serif;
    color: var(--ink); background: var(--white);
  }
  .site { position: relative; width: 1030px; height: 1200px; }

  .site-header { height: 73px; position: relative; border-bottom: 1px solid #e2e2e2; }
  .brand {
    position: absolute; left: 148px; top: 30px;
    font-size: 25px; font-weight: 600; letter-spacing: 0.5px; color: var(--ink); line-height: 1;
  }
  .main-nav { position: absolute; right: 155px; top: 36px; display: flex; gap: 20px; }
  .nav-item { display: flex; align-items: center; gap: 8px; font-size: 10px; color: var(--ink); text-decoration: none; }
  .nav-item svg { width: 22px; height: 22px; }

  .search-band { height: 242px; background: var(--green); position: relative; }
  .field {
    position: absolute; width: 353px; height: 35px; background: var(--white);
    font-size: 12px; font-style: italic; font-weight: 300; color: var(--muted);
    padding: 12px 12px; line-height: 1;
  }
  .field::after {
    content: ""; position: absolute; right: 12px; top: 15px;
    border-left: 4px solid transparent; border-right: 4px solid transparent; border-top: 6px solid var(--ink);
  }
  .col-a { left: 137px; } .col-b { left: 521px; }
  .row-1 { top: 39px; } .row-2 { top: 96px; } .row-3 { top: 152px; }
  .advance-search {
    position: absolute; left: 732px; top: 202px; display: flex; align-items: center; gap: 8px;
    color: var(--white); font-size: 12.5px; font-style: italic; font-weight: 300;
  }

  .results-intro { height: 43px; padding: 12px 0 0 138px; font-size: 20.5px; font-weight: 400; }
  .results {
    background: var(--page); height: 802px; padding: 11px 0 0 137px;
    border-top: 1px solid #e3e4dc;
  }
  .listing {
    width: 737px; height: 229px; background: var(--card); border: 1px solid var(--card-line);
    position: relative; margin-bottom: 28px;
  }
  .listing-head {
    height: 38px; background: var(--white); display: flex; justify-content: space-between; align-items: center;
    padding: 0 8px 0 15px;
  }
  .listing-title { font-size: 20.5px; font-weight: 400; letter-spacing: 0.2px; }
  .listing-offer { font-size: 12px; color: var(--green-text); margin-top: 4px; }
  .thumb {
    position: absolute; left: 24px; top: 53px; width: 107px; height: 81px; background: var(--white);
    display: flex; align-items: center; justify-content: center; font-size: 11px; color: #c9a3a8;
  }
  .specs, .dealer { position: absolute; top: 58px; font-size: 12px; line-height: 18px; }
  .specs { left: 150px; }
  .dealer { left: 294px; top: 52px; }
  .pricing { position: absolute; left: 535px; top: 52px; font-size: 12px; line-height: 18px; width: 190px; }
  .pricing-note { font-weight: 700; color: var(--green-text); }
  .price-cols { display: flex; }
  .price-cols div { width: 107px; }
  .price-value { color: var(--green-text); font-size: 12.5px; }
  .comments { position: absolute; left: 23px; top: 150px; width: 700px; }
  .comments-label { font-size: 12.5px; line-height: 15px; }
  .comments-text { font-size: 9px; line-height: 12.5px; }
  .more-button {
    position: absolute; left: 543px; top: 193px; width: 138px; height: 27px; background: var(--button);
    color: var(--white); font-size: 13.5px; font-weight: 300; display: flex; align-items: center; justify-content: center;
  }

  .site-footer {
    position: absolute; left: 0; top: 1158px; width: 1030px; height: 42px; border-top: 1px solid #e6e6e6;
  }
  .footer-links { position: absolute; left: 147px; top: 15px; display: flex; gap: 12px; font-size: 10px; }
  .footer-links a { color: var(--green-text); text-decoration: none; }
  .social { position: absolute; left: 810px; top: 12px; display: flex; gap: 3px; }
  .social span { width: 12px; height: 12px; border-radius: 50%; background: var(--social); display: block; }
</style>
</head>
<body>
<div class="site">
  <header class="site-header">
    <div class="brand">MOTORBAYHUB</div>
    <nav class="main-nav">
      <a class="nav-item" href="#">
        <svg viewBox="0 0 24 24" fill="none" stroke="#1c1c1c" stroke-width="1.8"><path d="M3 11 12 3l9 8"/><path d="M5.5 9v12h5v-6h3v6h5V9"/></svg>Home</a>
      <a class="nav-item" href="#">
        <svg viewBox="0 0 24 24" fill="none" stroke="#1c1c1c" stroke-width="1.8"><path d="M5 3h14v13l-5 5H5z"/><path d="M8 8h8M8 12h8M14 21v-5h5"/></svg>Watch List</a>
      <a class="nav-item" href="#">
        <svg viewBox="0 0 24 24" fill="none" stroke="#1c1c1c" stroke-width="1.8"><rect x="5" y="11" width="14" height="10"/><path d="M8 11V7a4 4 0 0 1 8 0"/></svg>Login Here</a>
    </nav>
  </header>

  <section class="search-band">
    <div class="field col-a row-1">Enter Make</div>
    <div class="field col-b row-1">Enter Model</div>
    <div class="field col-a row-2">Enter Price</div>
    <div class="field col-b row-2">Enter Age</div>
    <div class="field col-a row-3">Enter Body type</div>
    <div class="field col-b row-3">Enter a keyword</div>
    <div class="advance-search">
      <svg width="26" height="26" viewBox="0 0 26 26" fill="none" stroke="#fff" stroke-width="1.8"><circle cx="11" cy="11" r="8"/><path d="M17 17l7 7"/></svg>
      Advance Search
    </div>
  </section>

  <h2 class="results-intro">Search Results listed below:</h2>

  <main class="results">
    <article class="listing">
      <div class="listing-head"><h3 class="listing-title">2013 ALDERN KESTREL SPORT DCI</h3><span class="listing-offer">Buy it for $13570 or Please a Bid</span></div>
      <div class="thumb" role="img" aria-label="Vehicle photo">image</div>
      <div class="specs">2014<br>96000 Miles<br>Automatic<br>Black</div>
      <div class="dealer">Northgate Motors<br>127 Miles Away</div>
      <div class="pricing"><div class="pricing-note">Trying to deal my customer</div>
        <div class="price-cols"><div>Trade Price<br><span class="price-value">$14,500</span></div><div>Retail Price<br><span class="price-value">$16,900</span></div></div></div>
      <div class="comments"><div class="comments-label">Dealer Comments:</div>
        <p class="comments-text">Prepared for retail, Aldern GB plus 1 private owner, serviced twice at Aldern at 7k and 18k-- 2keys available. Not yet due an MOT Prepared for retail, Aldern GB plus 1 private owner, serviced twice at Aldern at 7k and 18k-- 2keys available. Not yet due an MOT</p></div>
      <div class="more-button">More Information</div>
    </article>

    <article class="listing">
      <div class="listing-head"><h3 class="listing-title">2013 ALDERN KESTREL SPORT DCI</h3><span class="listing-offer">Buy it for $13570 or Please a Bid</span></div>
      <div class="thumb" role="img" aria-label="Vehicle photo">image</div>
      <div class="specs">2014<br>96000 Miles<br>Automatic<br>Black</div>
      <div class="dealer">Northgate Motors<br>127 Miles Away</div>
      <div class="pricing"><div class="pricing-note">Trying to deal my customer</div>
        <div class="price-cols"><div>Trade Price<br><span class="price-value">$14,500</span></div><div>Retail Price<br><span class="price-value">$16,900</span></div></div></div>
      <div class="comments"><div class="comments-label">Dealer Comments:</div>
        <p class="comments-text">Prepared for retail, Aldern GB plus 1 private owner, serviced twice at Aldern at 7k and 18k-- 2keys available. Not yet due an MOT Prepared for retail, Aldern GB plus 1 private owner, serviced twice at Aldern at 7k and 18k-- 2keys available. Not yet due an MOT</p></div>
      <div class="more-button">More Information</div>
    </article>

    <article class="listing">
      <div class="listing-head"><h3 class="listing-title">2013 ALDERN KESTREL SPORT DCI</h3><span class="listing-offer">Buy it for $13570 or Please a Bid</span></div>
      <div class="thumb" role="img" aria-label="Vehicle photo">image</div>
      <div class="specs">2014<br>96000 Miles<br>Automatic<br>Black</div>
      <div class="dealer">Northgate Motors<br>127 Miles Away</div>
      <div class="pricing"><div class="pricing-note">Trying to deal my customer</div>
        <div class="price-cols"><div>Trade Price<br><span class="price-value">$14,500</span></div><div>Retail Price<br><span class="price-value">$16,900</span></div></div></div>
      <div class="comments"><div class="comments-label">Dealer Comments:</div>
        <p class="comments-text">Prepared for retail, Aldern GB plus 1 private owner, serviced twice at Aldern at 7k and 18k-- 2keys available. Not yet due an MOT Prepared for retail, Aldern GB plus 1 private owner, serviced twice at Aldern at 7k and 18k-- 2keys available. Not yet due an MOT</p></div>
      <div class="more-button">More Information</div>
    </article>
  </main>

  <footer class="site-footer">
    <nav class="footer-links">
      <a href="#">Contact us</a><a href="#">About us</a><a href="#">Legal info</a><a href="#">Privacy Policy</a><a href="#">Terms &amp; Conditions</a>
    </nav>
    <div class="social" aria-label="Social links"><span></span><span></span><span></span><span></span></div>
  </footer>
</div>
</body>
</html>
```